Neuroscience laboratory website

The "Signal, Thought and Cortex Lab" (aka, SoTiC Lab) is looking for a web site design. We are a cognitive neuroscience of language laboratory, which means we study the brain circuits involved in language comprehension. We need a professional-looking web presence where we can introduce the kind of research we do, list our publications, present our research team, present the current experiments that are being conducted and present our lab blog. Our current web site is displayed at http://sotic-lab.examplehost.io/sotic.lab.examplehost.io/. The new design should be a net improvement over the existing one.
Updates

Target Market(s)

Primary audience will be other academics and university-age students interested in learning more about the lab, but it should also target the general adult public based in western countries.

Industry/Entity Type

Laboratory

Colors

Designer to choose colors to be used in the design.

Requirements
Nice to have
• It would be nice if the design could be informed by at least one of all the following concepts: Human languages/scripts, mind, brain, neuroimaging and brain signals (like electroencephalogram), neuroscience, science, knowledge.

Word or visual play with the acronym of the lab (SoTiC) would be permissable, if a good idea can be extracted out of it.
Should not have
• Design should have a clean background. It should use large framing images very sparingly, if at all.

```html
<!DOCTYPE html>
<html lang="en">
<head>
<meta charset="utf-8">
<title>Signal, Thought and Cortex Lab — The Lab</title>
<link href="https://fonts.googleapis.com/css2?family=PT+Sans+Narrow:wght@400;700&family=Dancing+Script&display=swap" rel="stylesheet">
<style>
  :root {
    --lavender: #9d98c7;
    --lavender-dark: #8e88bb;
    --ink: #1a1a1a;
    --body: #4a4a4a;
    --muted: #7a7a7a;
    --footer-bg: #ebebeb;
    --white: #ffffff;
    --nav-shade: #e4e4e4;
  }
  * { box-sizing: border-box; margin: 0; padding: 0; }
  html, body { width: 985px; height: 1200px; overflow: hidden; background: var(--white); }
  body { position: relative; font-family: "PT Sans Narrow", "Arial Narrow", sans-serif; color: var(--body); }
  .abs { position: absolute; }

  /* header */
  .brand { left: 128px; top: 8px; width: 170px; height: 46px;
    background: linear-gradient(90deg, rgba(240,240,240,0), #f1f1f1 40%, rgba(240,240,240,0)); }
  .brand-name { left: 128px; top: 47px; width: 170px; text-align: center; font-size: 13px; color: var(--lavender); }
  .nav-shade { top: 0; width: 34px; height: 74px; background: linear-gradient(90deg, var(--nav-shade), rgba(255,255,255,0)); }
  .nav-item { top: 25px; font-size: 13.5px; color: var(--ink); transform: translateX(-50%); }

  /* left column */
  .page-title { left: 139px; top: 106px; font-size: 65px; font-weight: 700; color: var(--lavender); letter-spacing: -1px; }
  .lead { left: 140px; top: 191px; width: 312px; font-size: 17.5px; line-height: 18.6px; font-weight: 700; color: var(--ink); letter-spacing: -0.2px; }
  .copy { font-size: 12.8px; line-height: 15.4px; color: var(--body); letter-spacing: -0.25px; }
  .intro { left: 140px; top: 333px; width: 322px; }
  .brain-visual { left: 147px; top: 489px; width: 310px; height: 257px;
    background: radial-gradient(ellipse at 42% 38%, #f08a2a 0%, #c9562a 14%, #2f7be0 30%, #0e3a8c 52%, #000 72%); }
  .closing { left: 140px; top: 785px; width: 332px; }

  /* right column */
  .section-title { font-size: 18.5px; font-weight: 700; color: var(--lavender); }
  .methods-title { left: 505px; top: 133px; }
  .methods { left: 505px; top: 166px; width: 333px; }
  .pull-quote { left: 513px; top: 337px; width: 312px; height: 180px; background: var(--lavender);
    padding: 24px 14px 0 23px; color: var(--white); font-style: italic; font-size: 21px; line-height: 24px; letter-spacing: -0.3px; }
  .fine { left: 525px; top: 549px; width: 300px; font-size: 7.4px; line-height: 10.6px; color: var(--body); }
  .experiments-title { left: 524px; top: 624px; }
  .experiment-name { font-size: 13.5px; font-weight: 700; color: var(--ink); }
  .exp-1-name { left: 524px; top: 660px; }
  .exp-1 { left: 524px; top: 679px; width: 316px; font-size: 11.1px; line-height: 13.9px; letter-spacing: -0.2px; }
  .exp-2-name { left: 524px; top: 782px; }
  .exp-2 { left: 524px; top: 801px; width: 316px; font-size: 11.1px; line-height: 13.9px; letter-spacing: -0.2px; }

  /* footer */
  .footer { left: 0; top: 949px; width: 985px; height: 227px; background: var(--footer-bg); }
  .footer-glow { left: 150px; top: 940px; width: 430px; height: 10px;
    background: radial-gradient(ellipse at 50% 100%, #dcdcdc, rgba(235,235,235,0) 70%); }
  .quote-mark { left: 349px; top: 927px; width: 31px; height: 31px; border-radius: 50%; background: var(--white);
    box-shadow: 0 1px 3px rgba(0,0,0,.15); }
  .portrait { left: 156px; top: 995px; width: 72px; height: 78px; border: 4px solid var(--white);
    box-shadow: 0 1px 4px rgba(0,0,0,.25); border-radius: 3px;
    background: linear-gradient(160deg, #a9c6e6, #d9b39a 60%, #9a7b66); }
  .testimonial { left: 263px; top: 1002px; width: 285px; font-size: 11.2px; line-height: 13.6px; font-style: italic; color: var(--body); letter-spacing: -0.1px; }
  .signature { left: 163px; top: 1095px; font-family: "Dancing Script", cursive; font-size: 15px; color: var(--body); }
  .signature-role { left: 177px; top: 1115px; font-size: 7px; color: var(--lavender); }
  .slider-dots { left: 262px; top: 1099px; }
  .get-social { left: 385px; top: 1096px; font-size: 9.5px; color: var(--ink); }
  .social { left: 431px; top: 1092px; }
  .divider { left: 581px; top: 973px; width: 0; height: 168px; border-left: 1px dotted #8a8a8a; }
  .subscribe-title { left: 620px; top: 981px; width: 220px; text-align: center; font-size: 15px; font-weight: 700; color: var(--lavender); }
  .subscribe-sub { left: 620px; top: 999px; width: 220px; text-align: center; font-size: 13px; color: var(--muted); }
  .email-field { left: 634px; top: 1034px; width: 195px; height: 27px; background: var(--white); border: 1px solid #dcdcdc; }
  .subscribe-note { left: 642px; top: 1073px; width: 190px; font-size: 9px; line-height: 10.4px; font-style: italic; color: var(--muted); }
  .subscribe-btn { left: 675px; top: 1119px; width: 114px; height: 27px; background: var(--lavender);
    color: var(--white); font-weight: 700; font-size: 13.5px; text-align: center; line-height: 27px;
    box-shadow: 0 1px 2px rgba(0,0,0,.2); }

  .legal-bar { left: 0; top: 1176px; width: 985px; height: 24px; background: var(--lavender); }
  .legal { top: 1183px; font-size: 8px; color: var(--white); }
  .legal-links { left: 139px; }
  .copyright { right: 134px; }
</style>
</head>
<body>
  <header>
    <div class="abs brand"></div>
    <div class="abs brand-name">Signal, Thought and Cortex Lab</div>
    <div class="abs nav-shade" style="left:399px"></div>
    <div class="abs nav-shade" style="left:488px"></div>
    <div class="abs nav-shade" style="left:587px"></div>
    <div class="abs nav-shade" style="left:690px"></div>
    <div class="abs nav-shade" style="left:776px"></div>
    <nav>
      <span class="abs nav-item" style="left:352px">Home</span>
      <span class="abs nav-item" style="left:447px">People</span>
      <span class="abs nav-item" style="left:541px">Publications</span>
      <span class="abs nav-item" style="left:637px">Research</span>
      <span class="abs nav-item" style="left:734px">Blog</span>
      <span class="abs nav-item" style="left:826px">Codebase</span>
    </nav>
  </header>

  <main>
    <h1 class="abs page-title">The Lab</h1>
    <p class="abs lead">Language is a complex mental faculty, recruiting and integrating several interacting representa­tional and computational architectures in the mind. At the Signal, Thought and Cortex Lab (SoTiC Lab), we investigate the nature of the cognitive and neural architecture that supports the human</p>
    <p class="abs copy intro">Language is a complex mental faculty, recruiting and integrating several interacting representational and computational architectures in the mind. At the Signal, Thought and Cortex Lab (SoTiC Lab), we investigate the nature of the cognitive and neural architecture that supports the human language system and how it interfaces with other cognitive faculties. We combine insights from linguistic theory, processing models and what is known about their neurobiological underpinnings in order to guide our research questions.</p>
    <div class="abs brain-visual" role="img" aria-label="Illustration of a glowing human head and brain in blue and orange on black"></div>
    <p class="abs copy closing">Temporibus autem quibusdam et aut officiis debitis aut rerum necessitatibus saepe eveniet ut et voluptates repudiandae sint et molestiae non recusandae. Itaque earum rerum hic tenetur a sapiente delectus, ut aut reiciendis voluptati­bus maiores alias consequatur aut perferendis doloribus asperiores repellat.</p>

    <h2 class="abs section-title methods-title">The research methods</h2>
    <p class="abs copy methods">The lab houses several behavioral testing stations, as well as a 128-channel EEG system (CortexAmp DX, by NeuroWare Systems, Germany). The lab is also affili­ated with the Neural Speech Research Lab, which houses a state-of-the-art 208-channel whole-head MEG system (by the Halvorsen Institute of Technol­ogy, Japan), allowing for unimodal MEG recordings as well as concurrent EEG-MEG recordings with up to 64 EEG channels. In addition, a state-of-the-art fMRI facility is currently under construction in the new NIU-AQ campus in Marrow Island, which will expand the repertoire of brain imaging research that can be carried out in the lab.</p>
    <blockquote class="abs pull-quote">Nam libero tempore, cum soluta nobis est eligendi optio cumque nihil impedit quo minus id quod maxime placeat facere possimus, omnis voluptas assu­menda est, omnis dolor repellendus.</blockquote>
    <p class="abs fine">Temporibus autem quibusdam et aut officiis debitis aut rerum necessitatibus saepe eveniet ut et voluptates repudiandae sint et molestiae non recusandae. Itaque earum rerum hic tenetur a sapiente delectus, ut aut reiciendis voluptatibus maiores alias consequatur aut perferendis doloribus asperiores repellat.</p>

    <h2 class="abs section-title experiments-title">Current lab experiments</h2>
    <h3 class="abs experiment-name exp-1-name">Speech sounds</h3>
    <p class="abs copy exp-1">At vero eos et accusamus et iusto odio dignissimos ducimus qui blanditiis praesentium voluptatum deleniti atque corrupti quos dolores et quas molestias excepturi sint occaecati cupiditate non provident, similique sunt in culpa qui officia deserunt mollitia animi, id est laborum et dolorum fuga. Et harum quidem rerum facilis est et expedita distinctio.</p>
    <h3 class="abs experiment-name exp-2-name">Sentence comprehension in English</h3>
    <p class="abs copy exp-2">At vero eos et accusamus et iusto odio dignissimos ducimus qui blanditiis praesentium voluptatum deleniti atque corrupti quos dolores et quas molestias excepturi sint occaecati cupiditate non provident, similique sunt in culpa qui officia deserunt mollitia animi, id est laborum et dolorum fuga. Et harum quidem rerum facilis est et expedita distinctio.</p>
  </main>

  <footer>
    <div class="abs footer"></div>
    <div class="abs footer-glow"></div>
    <div class="abs quote-mark">
      <svg width="31" height="31" viewBox="0 0 31 31" aria-hidden="true">
        <text x="15.5" y="27" text-anchor="middle" font-family="Georgia, serif" font-size="26" font-weight="700" fill="#9d98c7">&#8220;</text>
      </svg>
    </div>
    <div class="abs portrait" role="img" aria-label="Portrait photo of the quoted researcher"></div>
    <p class="abs testimonial">Sed ut perspiciatis unde omnis iste natus sit voluptatem accusan­tium doloremque laudantium, totam rem aperiam, eaque ipsa quae ab illo inventore veritatis et quasi . Sed ut perspiciatis unde omnis iste natus sit voluptatem accusantium.</p>
    <div class="abs signature">- Jane Roe</div>
    <div class="abs signature-role">Lorem Ipsum Elit</div>
    <svg class="abs slider-dots" width="36" height="10" viewBox="0 0 36 10" aria-hidden="true">
      <circle cx="5" cy="5" r="4" fill="#c4c4c4"/>
      <circle cx="16" cy="5" r="4" fill="#d6d6d6"/>
      <circle cx="27" cy="5" r="4" fill="#d6d6d6"/>
    </svg>
    <span class="abs get-social">Get Social</span>
    <svg class="abs social" width="106" height="21" viewBox="0 0 106 21" aria-label="Social links">
      <rect x="0" y="0" width="19" height="19" rx="4" fill="#9d98c7"/>
      <rect x="21.5" y="0" width="19" height="19" rx="4" fill="#9d98c7"/>
      <rect x="43" y="0" width="19" height="19" rx="4" fill="#9d98c7"/>
      <rect x="64.5" y="0" width="19" height="19" rx="4" fill="#9d98c7"/>
      <rect x="86" y="0" width="19" height="19" rx="4" fill="#9d98c7"/>
    </svg>
    <div class="abs divider"></div>
    <div class="abs subscribe-title">SUBSCRIBE TO OUR NEWSLETTER</div>
    <div class="abs subscribe-sub">Lorem Ipsum Consectetur Adipiscing Elit</div>
    <div class="abs email-field"></div>
    <p class="abs subscribe-note">Sed ut perspiciatis unde omnis iste natus sit voluptatem accusantium. Sed ut perspiciatis unde omnis.</p>
    <div class="abs subscribe-btn">SUBSCRIBE</div>

    <div class="abs legal-bar"></div>
    <div class="abs legal legal-links">Terms of the | Privacy Policy</div>
    <div class="abs legal copyright">Copyright © 2014. All Rights Reserved.</div>
  </footer>
</body>
</html>
```